Software static HTML page design

We need 5 static HTML pages designed for our current software startup - TallyNest. All details are attached in a document for consideration.

Target Market(s)

Sporting clubs/University clubs

Industry/Entity Type

Software

Number of Pages Required

5+ page

Font styles to use
Sans Serif

Colors
33a6d7
85cae6
86cfc6
33b8a4
ffffff

```html
<!DOCTYPE html>
<html lang="en">
<head>
<meta charset="utf-8">
<title>TallyNest – Pricing</title>
<link rel="stylesheet" href="https://fonts.googleapis.com/css2?family=Source+Sans+3:wght@300;400;600;700&display=swap">
<style>
:root{
  --blue:#33a6d7;
  --sky:#85cae6;
  --mint:#86cfc6;
  --teal:#33b8a4;
  --white:#ffffff;
  --ink:#333333;
  --muted:#555555;
  --line:#d6d6d6;
  --social:#3b5998;
  --hero-top:#9fd6cf;
  --hero-bottom:#5bb3a5;
}
*{box-sizing:border-box;margin:0;padding:0}
html,body{width:1200px;height:952px;overflow:hidden;background:var(--white)}
body{font-family:"Source Sans 3",sans-serif;color:var(--ink);position:relative}
.hero-art{position:absolute;left:0;top:0;width:1200px;height:460px}
.brand{position:absolute;display:flex;align-items:center;gap:6px;font-size:20px;font-weight:600;letter-spacing:.5px}
.brand-mark{width:14px;height:14px}
.brand--header{left:250px;top:20px;color:var(--white)}
.brand--header .brand-mark{background:var(--white)}
.brand--footer{left:250px;top:886px;color:var(--blue)}
.brand--footer .brand-mark{background:var(--blue)}
.nav a,.nav span{position:absolute;top:27px;font-size:11px;color:var(--white);text-decoration:none;transform:translateX(-50%)}
.nav .is-active{top:22px;height:24px;width:51px;background:var(--white);color:var(--teal);display:flex;align-items:center;justify-content:center;transform:none}
.hero-title{position:absolute;left:246px;top:174px;font-size:36px;font-weight:300;line-height:38px;color:var(--white);letter-spacing:-.5px}
.auth-card{position:absolute;left:662px;top:112px;width:288px;height:272px;background:var(--white);box-shadow:0 2px 6px rgba(0,0,0,.15)}
.auth-tabs{position:absolute;left:14px;top:20px;width:260px;height:28px;border-bottom:2px solid var(--line);display:flex}
.auth-tab{flex:1;text-align:center;font-size:14px;color:var(--ink)}
.auth-tab.is-active{border-bottom:2px solid var(--muted);margin-bottom:-2px}
.social-btn{position:absolute;left:14px;top:61px;width:260px;height:24px;background:var(--social);color:var(--white);font-size:8px;font-weight:700;display:flex;align-items:center}
.social-btn .icon{width:28px;height:24px;background:rgba(0,0,0,.25);margin-right:12px;display:flex;align-items:center;justify-content:center}
.divider-or{position:absolute;top:102px;width:100%;text-align:center;font-size:8px;font-weight:600}
.field{position:absolute;left:14px;width:260px;height:26px;border:1px solid var(--line);border-radius:2px;font-size:8px;color:var(--muted);padding-left:11px;display:flex;align-items:center}
.field--email{top:125px}
.field--password{top:158px}
.forgot{position:absolute;top:198px;width:100%;text-align:center;font-size:8px;font-weight:600}
.submit-btn{position:absolute;left:14px;top:223px;width:260px;height:25px;background:var(--blue);color:var(--white);font-size:8px;font-weight:600;display:flex;align-items:center;justify-content:center;box-shadow:0 1px 2px rgba(0,0,0,.2)}
.section-title{position:absolute;top:446px;width:100%;text-align:center;font-size:22px;font-weight:700;color:var(--teal)}
.section-lead{position:absolute;top:491px;width:100%;text-align:center;font-size:17px;font-weight:300;color:var(--ink)}
.price-card{position:absolute;color:var(--white);text-align:center;box-shadow:0 1px 4px rgba(0,0,0,.15)}
.price-card--intl{left:249px;top:539px;width:351px;height:219px;background:var(--mint)}
.price-card--domestic{left:600px;top:563px;width:351px;height:171px;background:var(--teal)}
.plan{position:absolute;width:100%;font-size:13px}
.plan-rule{position:absolute;left:70px;width:212px;height:1px;background:rgba(255,255,255,.8)}
.rate{position:absolute;width:100%;font-size:41px;font-weight:700;line-height:1}
.rate-note{position:absolute;width:100%;font-size:14px}
.price-card--intl .plan{top:21px}
.price-card--intl .plan-rule{top:57px}
.price-card--intl .rate{top:91px}
.price-card--intl .rate-note{top:148px}
.price-card--domestic .plan{top:15px}
.price-card--domestic .plan-rule{top:51px}
.price-card--domestic .rate{top:74px;left:-7px}
.price-card--domestic .rate-note{top:130px;left:-7px}
.tax-note{position:absolute;top:789px;width:100%;text-align:center;font-size:17px;font-weight:300;color:var(--muted)}
.legal{position:absolute;left:430px;top:891px;font-size:10px;color:var(--muted)}
.credit{position:absolute;right:249px;top:891px;font-size:10px;color:var(--muted)}
.credit strong{color:var(--ink);font-weight:700}
</style>
</head>
<body>
<svg class="hero-art" viewBox="0 0 1200 460" role="img" aria-label="Teal-tinted photo of a running track with lane lines and painted lane number">
  <defs>
    <linearGradient id="heroFill" x1="0" y1="0" x2="0.3" y2="1">
      <stop offset="0" stop-color="var(--hero-top)"/>
      <stop offset="1" stop-color="var(--hero-bottom)"/>
    </linearGradient>
  </defs>
  <polygon points="0,0 1200,0 1200,196 248,404 248,452 0,328" fill="url(#heroFill)"/>
</svg>

<div class="brand brand--header"><span class="brand-mark"></span>TallyNest</div>

<nav class="nav">
  <a style="left:426px">Home</a>
  <a style="left:481px">Features</a>
  <a class="is-active" style="left:513px">Pricing</a>
  <a style="left:601px">Get Started</a>
  <a style="left:672px">Contact us</a>
  <a style="left:759px">Club</a>
  <span style="left:782px">I</span>
  <a style="left:810px">Events</a>
  <a style="left:886px">Login</a>
  <span style="left:908px">\</span>
  <a style="left:941px">Sign Up →</a>
</nav>

<h1 class="hero-title">All features are included.<br>Only pay for transactions<br>you process.</h1>

<div class="auth-card">
  <div class="auth-tabs">
    <div class="auth-tab is-active">Log In</div>
    <div class="auth-tab">Sign Up</div>
  </div>
  <div class="social-btn"><span class="icon"></span>Log In with Friendlink</div>
  <div class="divider-or">or</div>
  <div class="field field--email">you@example.com</div>
  <div class="field field--password">your password</div>
  <div class="forgot">Don't remember your password?</div>
  <div class="submit-btn">Log In</div>
</div>

<h2 class="section-title">Pricing</h2>
<p class="section-lead">All features are included. Only pay for transactions you process.</p>

<div class="price-card price-card--intl">
  <div class="plan">PAY AS YOU GO</div>
  <div class="plan-rule"></div>
  <div class="rate">5.40% + $0.30</div>
  <div class="rate-note">for international cards.</div>
</div>
<div class="price-card price-card--domestic">
  <div class="plan">PAY AS YOU GO</div>
  <div class="plan-rule"></div>
  <div class="rate">4.50% + $0.30</div>
  <div class="rate-note">for domestic cards.</div>
</div>

<p class="tax-note">GST included.</p>

<footer>
  <div class="brand brand--footer"><span class="brand-mark"></span>TallyNest</div>
  <div class="legal">2017 © TallyNest Pty Ltd. All Rights Reserved. &nbsp;&nbsp; I &nbsp;&nbsp; ABN 12 345 678 901</div>
  <div class="credit">Built By <strong>Brightline Studio</strong></div>
</footer>
</body>
</html>
```